VOIP company busioness card redesign

Redesign business card to match our new logo and marketing material. Should include logo on one side and contact information on other side.

We like modern and clean

Industry/Entity Type

Phone Company

Contact Information for Business Card

One side should be logo other side should include contact info
Name
Phone Number
email
website

Font styles to use
Other font styles liked:
• dont care

Requirements
Must have
• Modern sleek design that works with our logo

```html
<!DOCTYPE html>
<html lang="en">
<head>
<meta charset="utf-8">
<title>Nuvolink Business Card</title>
<link href="https://fonts.googleapis.com/css2?family=Arimo:wght@400;700&display=swap" rel="stylesheet">
<style>
  :root {
    --backdrop: #e9e9ea;
    --paper: #f1f1f0;
    --brand-blue: #1b9bd4;
    --ink: #2b2b2b;
    --muted: #a9b0b4;
    --white: #ffffff;
  }
  * { margin: 0; padding: 0; box-sizing: border-box; }
  html, body {
    width: 1200px; height: 1083px; overflow: hidden;
    background: var(--backdrop);
    font-family: "Arimo", Arial, sans-serif;
  }
  .canvas { position: relative; width: 1200px; height: 1083px; }
  .card {
    position: absolute; width: 520px; height: 297px;
    box-shadow: 0 10px 24px rgba(0,0,0,0.12);
    overflow: hidden;
  }
  /* contact side */
  .card-contact { left: 90px; top: 170px; background: var(--paper); }
  .card-contact .brand {
    position: absolute; left: 34px; top: 30px;
    font-size: 30px; font-weight: 700; color: var(--brand-blue);
    letter-spacing: -0.5px; line-height: 1;
  }
  .card-contact .brand-tagline {
    position: absolute; left: 36px; top: 64px;
    font-size: 8px; color: var(--muted);
  }
  .accent-stripe {
    position: absolute; left: 230px; right: 0; top: 112px; height: 9px;
    background: var(--brand-blue);
  }
  .accent-stripe::after {
    content: ""; position: absolute; right: 0; top: 0; width: 46px; height: 100%;
    background: var(--muted);
  }
  .contact-block { position: absolute; left: 120px; top: 136px; color: var(--ink); }
  .person-name { font-size: 19px; font-weight: 700; color: var(--brand-blue); line-height: 1.15; }
  .person-role { font-size: 13px; margin-top: 2px; line-height: 1.2; }
  .contact-line {
    display: flex; align-items: center; gap: 10px;
    font-size: 13px; line-height: 1.2; margin-top: 7px;
  }
  .contact-line svg { width: 14px; height: 14px; fill: var(--brand-blue); flex: none; }
  .contact-line.first { margin-top: 10px; }
  .web-band {
    position: absolute; left: 0; right: 0; bottom: 22px; height: 32px;
    background: var(--brand-blue); color: var(--white);
    font-size: 14px; font-weight: 700;
    display: flex; align-items: center; padding-left: 170px;
  }
  /* logo side */
  .card-logo {
    left: 590px; top: 560px; background: var(--brand-blue);
    display: flex; align-items: center; justify-content: center;
  }
  .logo-lockup { color: var(--white); text-align: left; }
  .logo-lockup .brand-row { display: flex; align-items: flex-end; gap: 6px; }
  .logo-lockup .brand { font-size: 54px; font-weight: 700; line-height: 1; letter-spacing: -1px; }
  .logo-lockup .brand-suffix { font-size: 11px; padding-bottom: 8px; }
  .logo-lockup .brand-tagline { font-size: 11px; margin-top: 4px; opacity: 0.9; }
</style>
</head>
<body>
<main class="canvas">
  <section class="card card-contact" aria-label="Contact side">
    <div class="brand">Nuvolink</div>
    <div class="brand-tagline">Cloud voice made simple</div>
    <div class="accent-stripe"></div>
    <div class="contact-block">
      <div class="person-name">Marcus Reed</div>
      <div class="person-role">Sales Manager</div>
      <div class="contact-line first">
        <svg viewBox="0 0 24 24" aria-hidden="true"><path d="M6.6 10.8c1.4 2.8 3.8 5.1 6.6 6.6l2.2-2.2c.3-.3.7-.4 1-.2 1.1.4 2.3.6 3.6.6.6 0 1 .4 1 1V20c0 .6-.4 1-1 1C10.6 21 3 13.4 3 4c0-.6.4-1 1-1h3.5c.6 0 1 .4 1 1 0 1.3.2 2.5.6 3.6.1.3 0 .7-.2 1z"/></svg>
        <span>1-855-555-0142</span>
      </div>
      <div class="contact-line">
        <svg viewBox="0 0 24 24" aria-hidden="true"><path d="M2 5h20v14H2z M2 5l10 8 10-8" stroke="#f1f1f0" stroke-width="1.6"/></svg>
        <span>sales@nuvolinkcomms.com</span>
      </div>
    </div>
    <div class="web-band">www.nuvolinkcomms.com</div>
  </section>

  <section class="card card-logo" aria-label="Logo side">
    <div class="logo-lockup">
      <div class="brand-row">
        <span class="brand">Nuvolink</span>
        <span class="brand-suffix">Comms</span>
      </div>
      <div class="brand-tagline">Clear Calls, Anywhere You Work</div>
    </div>
  </section>
</main>
</body>
</html>
```